Broschüre für ClipVerkauf-Mentor
Sehr schnelle und professionelle Umsetzung. Die Designerin hat inhaltlich mitgedacht und die einzelnen Elemente passend und kreativ platziert. Der Kontakt war außerdem sehr nett. Sehr zu empfehlen!
Zielgruppe
Ich bin Deutschlands erster ClipVerkauf-Mentor. Ich zeige Unternehmern, Selbstständigen und Vertrieblern wie sie mit persönlichen Videobotschaften mehr Interessen und Abschlüsse generieren.
Aufgabenstellung
Es soll eine Broschüre grafisch gestaltet werden, die als eBook sowie für den Druck verwendet werden kann.
Format DIN A 4.
Bereitgestellt werden folgende Unterlagen:
(1) Texte und Grob-Struktur in der entsprechenden Reihenfolge.
(2) Die Broschüre soll sich an der Struktur des beigefügten eBooks 'Homepage Tale Spark' orientieren.
(3) Fotos, Logo und Grafikelemente sind beigefügt. Zusätzliches Bildmaterial darf eingesetzt werden.
(4) Ein 'Brand Look' mit Farben, Schriftarten und Stil-Elementen ist beigefügt.
(5) Druckvorlage gemäß beigefügter Vorlage von Druckquelle. Für den Druck müssen es 20 oder 24 Seiten sein.
Bitte grafisch an meiner Website orientieren: www.mattenlohr.de

```html
<!DOCTYPE html>
<html lang="de">
<head>
<meta charset="utf-8">
<title>ClipVerkauf – Broschüre Titelseite</title>
<link rel="stylesheet" href="https://fonts.googleapis.com/css2?family=Poppins:wght@500;600;800&display=swap">
<style>
  :root {
    --stage: #e4e4e6;
    --paper: #f1f2f4;
    --forest: #2f5f4c;
    --mint: #82e0a6;
    --lime: #dbef63;
    --photo-warm: #8a6442;
    --photo-dark: #4a3526;
  }
  * { margin: 0; padding: 0; box-sizing: border-box; }
  html, body { width: 1200px; height: 1200px; overflow: hidden; background: var(--stage); }
  body { display: flex; align-items: center; justify-content: center; font-family: "Poppins", sans-serif; }

  .cover {
    position: relative;
    width: 778px;
    height: 1100px;
    background: var(--forest);
    overflow: hidden;
    box-shadow: 0 18px 40px rgba(0,0,0,0.18);
  }
  .cover-header {
    position: absolute; inset: 0 0 auto 0;
    height: 150px;
    background: var(--paper);
    display: flex; align-items: center;
    padding-left: 60px; gap: 18px;
  }
  .brand-dot {
    width: 54px; height: 54px; border-radius: 50%;
    background: var(--forest);
  }
  .brand-name {
    font-weight: 800; font-size: 26px; letter-spacing: 1.5px;
    color: var(--forest);
  }
  .accent-arc { position: absolute; inset: 0; }
  .cover-photo {
    position: absolute;
    left: 60px; top: 200px;
    width: 658px; height: 440px;
    background: linear-gradient(120deg, #c9b49a 0%, var(--photo-warm) 40%, var(--photo-dark) 75%, #b9ad9d 100%);
  }
  .cover-title {
    position: absolute; left: 60px; top: 680px;
    font-weight: 800; font-size: 72px; line-height: 1;
    color: var(--mint);
  }
  .cover-subtitle {
    position: absolute; left: 60px; top: 790px; width: 560px;
    font-weight: 500; font-size: 20px; line-height: 1.35;
    color: var(--lime);
  }
  .cover-author {
    position: absolute; left: 60px; top: 930px;
    font-weight: 500; font-size: 17px;
    color: var(--mint);
  }
</style>
</head>
<body>
  <article class="cover">
    <header class="cover-header">
      <span class="brand-dot"></span>
      <span class="brand-name">DR. MORITZ K. LOHR</span>
    </header>

    <svg class="accent-arc" width="778" height="1100" viewBox="0 0 778 1100" aria-hidden="true">
      <path d="M 599 620 A 340 340 0 0 1 655 1110" fill="none" stroke="var(--lime)" stroke-width="30"/>
    </svg>

    <div class="cover-photo" role="img" aria-label="Foto: Mann mit Headset winkt freundlich in die Kamera seines Laptops, Backsteinwand im Hintergrund"></div>

    <h1 class="cover-title">ClipVerkauf</h1>
    <p class="cover-subtitle">5 Bausteine, wie Du mit persönlichen Videobotschaften mehr Interessenten und Abschlüsse gewinnst.</p>
    <p class="cover-author">Dr. Moritz K. Lohr</p>
  </article>
</body>
</html>
```